Tranquil Pathway Business Card

Logo attached. (will be printing onto thick white/off white textured card)

Double sided business card for two Therapists working at Tranquil Pathway.

Require one design, but with different name and mobile numbers on each card.

Target Market(s)

Medical, Health

Industry/Entity Type

Business

Contact Information for Business Card

Need one business card design, but a separate card for each person - Colin Marchetti and Marieke de Boeckx.

FRONT OF CARD

Logo

Name (Colin Marchetti on one card, Marieke de Boeckx on the other)
Professional Clinical Hypnotherapist

Consulting Rooms (Near Lindqvist Hospital)
482 Brackenfield Road
Dunmore VIC 3987

Colin@TranquilPathway.example.au OR Marieke@TranquilPathway.example.au

Mobile: 0455 872 604 (for Colin) OR
Mobile: 0467 290 518 (for Marieke)

BACK OF CARD

Logo

Website: www.TranquilPathway.example.au

Phone: 1300 958 471

Requirements
Must have
• Text and logo only. No additiional graphics.

```html
<!DOCTYPE html>
<html lang="en">
<head>
<meta charset="utf-8">
<title>Tranquil Pathway Business Card</title>
<link href="https://fonts.googleapis.com/css2?family=Lato:wght@300;400;700;900&family=Open+Sans:wght@400;600&display=swap" rel="stylesheet">
<style>
  :root {
    --page-bg: #ecebe8;
    --brand-blue: #3a4a93;
    --brand-blue-dark: #2e3d80;
    --navy-text: #1f2d6b;
    --card-white: #fbfbfa;
    --rule-grey: #8a8a8a;
    --ring-grey: #9a9a9a;
    --body-grey: #6e6e6e;
    --soft-white: #e9ecf6;
    --muted-blue-text: #8d97c4;
  }
  * { box-sizing: border-box; margin: 0; padding: 0; }
  html, body { width: 1200px; height: 800px; overflow: hidden; }
  body {
    background: var(--page-bg);
    font-family: "Open Sans", Arial, sans-serif;
    position: relative;
  }
  .card {
    position: absolute;
    top: 257px;
    width: 500px;
    height: 286px;
    border-radius: 3px;
    box-shadow: 0 6px 18px rgba(0,0,0,0.14);
    overflow: hidden;
  }

  /* Back of card */
  .card--back {
    left: 60px;
    background: linear-gradient(160deg, var(--brand-blue) 0%, var(--brand-blue-dark) 100%);
    color: var(--soft-white);
  }
  .card--back .brand-mark {
    position: absolute;
    left: 52px;
    top: 83px;
    width: 120px;
    height: 120px;
    border-radius: 50%;
    background: var(--soft-white);
  }
  .card--back .brand-divider {
    position: absolute;
    left: 200px;
    top: 78px;
    width: 2px;
    height: 130px;
    background: var(--muted-blue-text);
  }
  .card--back .brand-name {
    position: absolute;
    left: 226px;
    top: 108px;
    font-family: "Lato", Arial, sans-serif;
    font-weight: 700;
    font-size: 30px;
    line-height: 36px;
    letter-spacing: 2px;
    text-transform: uppercase;
    color: var(--soft-white);
  }
  .card--back .website {
    position: absolute;
    left: 0;
    right: 0;
    bottom: 22px;
    text-align: center;
    font-size: 11px;
    letter-spacing: 1px;
    color: var(--muted-blue-text);
  }

  /* Front of card */
  .card--front {
    left: 640px;
    background: var(--card-white);
  }
  .card--front .logo-block {
    position: absolute;
    left: 24px;
    top: 60px;
    width: 130px;
    text-align: center;
  }
  .card--front .brand-mark {
    display: block;
    margin: 0 auto 12px;
    width: 100px;
    height: 100px;
    border-radius: 50%;
    background: var(--brand-blue);
  }
  .card--front .brand-name {
    font-family: "Open Sans", Arial, sans-serif;
    font-weight: 600;
    font-size: 12px;
    letter-spacing: 1px;
    text-transform: uppercase;
    color: var(--brand-blue);
  }
  .card--front .vertical-rule {
    position: absolute;
    left: 172px;
    top: 56px;
    width: 1.5px;
    height: 164px;
    background: var(--rule-grey);
  }
  .contact {
    position: absolute;
    left: 190px;
    top: 64px;
    right: 14px;
  }
  .contact .person-name {
    font-family: "Lato", Arial, sans-serif;
    font-weight: 900;
    font-size: 20px;
    letter-spacing: 0.5px;
    text-transform: uppercase;
    color: var(--navy-text);
    line-height: 24px;
  }
  .contact .person-title {
    font-size: 11.5px;
    color: var(--body-grey);
    margin-bottom: 10px;
  }
  .contact .line {
    display: flex;
    align-items: center;
    gap: 6px;
    font-size: 11.5px;
    line-height: 17px;
    color: var(--body-grey);
  }
  .contact .line svg { flex: 0 0 12px; }
  .contact .address {
    margin-top: 4px;
    font-size: 11.5px;
    line-height: 17px;
    color: var(--body-grey);
  }
</style>
</head>
<body>

  <section class="card card--back" aria-label="Back of business card">
    <span class="brand-mark" aria-hidden="true"></span>
    <span class="brand-divider" aria-hidden="true"></span>
    <p class="brand-name">Tranquil<br>Pathway</p>
    <p class="website">www.TranquilPathway.example.au</p>
  </section>

  <section class="card card--front" aria-label="Front of business card">
    <div class="logo-block">
      <span class="brand-mark" aria-hidden="true"></span>
      <p class="brand-name">Tranquil Pathway</p>
    </div>
    <span class="vertical-rule" aria-hidden="true"></span>
    <div class="contact">
      <p class="person-name">Colin Marchetti</p>
      <p class="person-title">Professional Clinical Hypnotherapist</p>
      <p class="line">
        <svg width="12" height="12" viewBox="0 0 12 12" aria-hidden="true">
          <rect width="12" height="12" rx="1.5" fill="var(--brand-blue)"/>
          <path d="M3.6 2.6 L5 2.6 L5.5 4.4 L4.6 5.1 Q5.4 6.8 6.9 7.4 L7.6 6.5 L9.4 7 L9.4 8.4 Q9.4 9.4 8.3 9.4 Q3 8.9 2.6 3.7 Q2.6 2.6 3.6 2.6 Z" fill="#fff"/>
        </svg>
        0455 872 604
      </p>
      <p class="line">
        <svg width="12" height="12" viewBox="0 0 12 12" aria-hidden="true">
          <rect width="12" height="12" rx="1.5" fill="var(--brand-blue)"/>
          <rect x="2.3" y="3.5" width="7.4" height="5" fill="none" stroke="#fff" stroke-width="1"/>
          <path d="M2.5 3.7 L6 6.3 L9.5 3.7" fill="none" stroke="#fff" stroke-width="1"/>
        </svg>
        Colin@TranquilPathway.example.au
      </p>
      <p class="address">
        Consulting Rooms (Near Lindqvist Hospital)<br>
        482 Brackenfield Road<br>
        Dunmore VIC 3987
      </p>
    </div>
  </section>

</body>
</html>
```